Letterhead Design Project

I need a simple, clean and corporate letterhead & follow-on letterhead.
The follow-on letterhead should just have the logo only.
Final File Specs:
Full Bleed Size (starting document size)
213 x 300 mm
2517 x 3544 pixels
* Finished artwork should use the full bleed dimensions for best results.
Document Trim Size (final size after being cut)
210 x 297 mm
2480 x 3508 pixels
* Please be sure to keep all text within the safe margin.
Resolution 300 DPI
Accepted file types:-
Adobe Acrobat 9 Document (*.pdf) (recommended)
Adobe Illustrator CS3 Artwork (*.ai) (recommended)
Adobe Photoshop CS3 Image (*.psd) (recommended)
Bitmap Image (*.bmp)
GIF Image (*.gif)
JPEG Image (*.jpg,*.jpeg)
Microsoft PowerPoint 2010 Document (*.ppt)
Microsoft Publisher 2010 Document (*.pub)
Microsoft Word 2010 Document (*.doc)
PCX Image (*.pcx)
PICT Image (*.pic,*.pict,*.pct)
PNG Image (*.png)
PostScript Document (*.ps)
TIF Image (*.tif,*.tiff)
Windows Enhanced Metafile (*.emf)
Windows Metafile (*.wmf)
Requirements
Must have
- My letterhead must have:-
- Logo
- ACN - 482 617 309
- address - Suite 8, 51 Hartwell Ave, Marlow Bay, NSW 2187
- phone - (02) 8371 5926
- fax - (02) 8352 6149
- email - info@brantorguard.com.au
- web - www.brantorguard.com.au
Follow-on letterhead should have the logo only

```html
<!DOCTYPE html>
<html lang="en">
<head>
<meta charset="utf-8">
<title>Brantor Asbestos &amp; Safety – Letterhead Set</title>
<link rel="stylesheet" href="https://fonts.googleapis.com/css2?family=Barlow:wght@400;500;600;700&display=swap">
<style>
  :root {
    --brand-green: #8dc63f;
    --brand-navy: #1d1f45;
    --ink: #26272b;
    --sheet: #ffffff;
    --sheet-edge: #9a9a9a;
    --backdrop-centre: #ffffff;
    --backdrop-edge: #d9d9db;
  }
  * { box-sizing: border-box; margin: 0; padding: 0; }
  html, body {
    width: 1200px;
    height: 857px;
    overflow: hidden;
  }
  body {
    position: relative;
    font-family: "Barlow", Arial, sans-serif;
    background: radial-gradient(ellipse 62% 62% at 50% 52%, var(--backdrop-centre) 55%, var(--backdrop-edge) 100%);
  }
  .sheet {
    position: absolute;
    top: 136px;
    width: 400px;
    height: 565px;
    background: var(--sheet);
    border: 1px solid var(--sheet-edge);
  }
  .sheet--first { left: 111px; }
  .sheet--follow-on { left: 651px; }

  .brand {
    position: absolute;
    left: 18px;
    top: 36px;
  }
  .brand__name {
    display: block;
    font-size: 27px;
    font-weight: 600;
    line-height: 27px;
    color: var(--brand-green);
    letter-spacing: -0.3px;
  }
  .brand__tagline {
    margin-top: 1px;
    font-size: 7.5px;
    font-weight: 600;
    letter-spacing: 0.15px;
    color: var(--brand-navy);
    white-space: nowrap;
  }

  .contact {
    position: absolute;
    left: 16px;
    top: 482px;
    padding-left: 4px;
    border-left: 3px solid var(--brand-green);
    padding-top: 8px;
    padding-bottom: 9px;
    list-style: none;
  }
  .contact__line {
    font-size: 6.6px;
    line-height: 8.7px;
    color: var(--ink);
    white-space: nowrap;
  }
  .contact__label {
    color: var(--brand-green);
    font-weight: 600;
  }
</style>
</head>
<body>

  <section class="sheet sheet--first" aria-label="First page letterhead">
    <div class="brand">
      <span class="brand__name">Brantor</span>
      <div class="brand__tagline">ASBESTOS &amp; SAFETY</div>
    </div>

    <ul class="contact">
      <li class="contact__line"><span class="contact__label">acn:</span> 482 617 309</li>
      <li class="contact__line"><span class="contact__label">add.:</span> Suite 8, 51 Hartwell Ave, Marlow Bay, NSW 2187</li>
      <li class="contact__line"><span class="contact__label">tel.:</span> (02) 8371 5926 | <span class="contact__label">fax.:</span> (02) 8352 6149</li>
      <li class="contact__line"><span class="contact__label">e-mail:</span> info@brantorguard.com.au</li>
      <li class="contact__line"><span class="contact__label">web:</span> www.brantorguard.com.au</li>
    </ul>
  </section>

  <section class="sheet sheet--follow-on" aria-label="Follow-on letterhead">
    <div class="brand">
      <span class="brand__name">Brantor</span>
      <div class="brand__tagline">ASBESTOS &amp; SAFETY</div>
    </div>
  </section>

</body>
</html>
```